High-end Oceanfront Real Estate Group Needs Clean, Modern Web Design

I’m looking for a clean, professional, modern and beautiful homepage web design for a Real Estate group in Southern California, USA.

The group/company is “Marlow on the Shore,” and they specialize in high end (i.e. expensive), oceanfront real estate in the Orange County area.

The look and feel of the page should accentuate the brand qualities: luxurious/expensive, professional, and beautiful (Orange County is one of the most beautiful areas in all the US and we would love the site to emphasize the beautiful beaches and scenery it has to offer).

Looks we like:
• www.brantleyhomesrealty.example
• www.keptbyfenwick.example -- I think the design is pretty out-dated in this site, but I like the organization/layout of the site

Header Tags (I don’t know if we can fit all of these, may need a side-menu, but I’d prefer header title only if possible):
• Welcome
• Featured Listings
• Previously Sold
• Sell
• Property Search
• Team
• Videos
• Blog
• Explore O.C.
• Contact

I have attached the beach and logo pics that we would like to use as the header, a few pictures of the team, and one sample home/view pic which can be used in any of the other sections (for pictures of the homes, just find expensive oceanfront houses and that will be fine).

I promise to provide feedback to each and every design submission. I appreciate the hard work that all of you are putting into your designs. There can be only one contest winner, but I hope to give all of you helpful feedback to submit the best designs possible!

Target Market(s)

Very wealthy home owners of oceanfront properties. These properties are worth several millions of dollars, and thus the site and brand needs to be targeted to very wealthy, successful individuals and families (both US and international buyers).

Industry/Entity Type

Real Estate

Number of Pages Required

2 page

Requirements
Must have
• I don’t want to give too many requirements, because I want to let you all be creative. However, here are the few Must Haves:
• Must submit 2 page designs (a home page and a sub page)
• Must use logo provided
• Focus is mostly on homes, but I would like to include some beach/ocean imagery as well
• The first “item” on the home page should be an accordion/slider which shows pictures of homes and with 1 line of text: “List with the Leader” and two link buttons: “Sell Your Home” and “Buy Your Home”
• Color palette needs to be mainly blues--to match ocean and sky blue
• Exported in all major formats (psd,ai,eps,png,jpeg,etc)
Nice to have
• We don’t necessarily need all of these, but would like to feature most:
• List of videos
• “Meet the Team”—brief team bios and pics
• Link(s) to Blog
• “List with the Leader” – section on why they should choose this firm
• Featured Listings
• Previously Sold

```html
<!DOCTYPE html>
<html lang="en">
<head>
<meta charset="utf-8">
<title>Marlow on the Shore</title>
<link rel="stylesheet" href="https://fonts.googleapis.com/css2?family=Advent+Pro:wght@200;300&family=Oswald:wght@300;400&family=Open+Sans:wght@400;700&display=swap">
<style>
  :root {
    --blue: #1a9be6;
    --blue-deep: #0b8ad6;
    --ink: #222222;
    --white: #ffffff;
    --grey-band: #eeeeee;
    --grey-panel: #e4e4e4;
    --card-border: #d2d2d2;
    --sage: #dfe3d2;
    --footer: #000000;
    --muted: #555555;
  }
  * { margin: 0; padding: 0; box-sizing: border-box; }
  html, body { width: 1200px; height: 2740px; overflow: hidden; }
  body { position: relative; background: var(--white); font-family: "Open Sans", sans-serif; color: var(--ink); }
  .abs { position: absolute; }

  /* Hero */
  .hero-photo { left: 0; top: 0; width: 1200px; height: 722px;
    background: linear-gradient(180deg, #2f5f97 0%, #4b7db0 22%, #6a9bc6 38%, #c9d8e2 50%, #93a8b6 58%, #7f8a8c 66%, #b7a78f 80%, #c9b89c 100%); }
  .brand-box { left: 489px; top: 15px; width: 221px; height: 155px; background: rgba(255,255,255,0.72);
    display: flex; align-items: center; justify-content: center; text-align: center; }
  .brand-name { font-family: "Advent Pro", sans-serif; font-weight: 300; font-size: 38px; line-height: 40px; color: #2a7fc2; letter-spacing: 1px; }
  .main-nav { left: 91px; top: 190px; width: 1020px; display: flex; justify-content: space-between;
    font-family: "Oswald", sans-serif; font-weight: 300; font-size: 18px; color: var(--white); text-transform: uppercase; }
  .main-nav .current { color: #111; font-weight: 400; }
  .hero-title { left: 0; top: 355px; width: 1200px; text-align: center; font-family: "Advent Pro", sans-serif;
    font-weight: 200; font-size: 56px; color: #1b1b1b; letter-spacing: 2px; }

  /* Intro video + highlights */
  .video-frame { left: 77px; top: 584px; width: 701px; height: 362px;
    background: linear-gradient(180deg, #7fb2dc 0%, #6c9f6a 30%, #4f8f3e 60%, #d8d4cb 85%, #9bb7a2 100%); }
  .play-btn { left: 374px; top: 742px; width: 98px; height: 62px; }
  .highlights { left: 778px; top: 584px; width: 343px; height: 362px; background: var(--grey-panel); }
  .highlight { position: absolute; left: 14px; display: flex; align-items: center; gap: 22px;
    font-family: "Oswald", sans-serif; font-weight: 400; font-size: 18px; color: var(--blue); }
  .highlight svg { width: 54px; height: 54px; flex: none; }

  /* List with the leader */
  .leader-photo { left: 0; top: 1001px; width: 1200px; height: 465px;
    background: linear-gradient(180deg, #8fbfe6 0%, #b9d4e6 12%, #4f8c4a 35%, #6ea55a 60%, #c9c2b2 85%, #5e7d52 100%); }
  .label-box { font-family: "Advent Pro", sans-serif; font-weight: 300; color: #1b1b1b; text-align: center; text-transform: uppercase; }
  .leader-title { left: 374px; top: 1074px; width: 453px; height: 73px; background: var(--white); font-size: 50px; line-height: 73px; }
  .sell-btn { left: 223px; top: 1280px; width: 246px; height: 64px; background: var(--white); font-size: 38px; line-height: 64px; }
  .buy-btn { left: 712px; top: 1280px; width: 247px; height: 64px; background: var(--sage); font-size: 38px; line-height: 64px; }

  /* Featured listing */
  .featured-band { left: 0; top: 1466px; width: 1200px; height: 460px; background: var(--grey-band); }
  .section-title { left: 0; width: 1200px; text-align: center; font-family: "Advent Pro", sans-serif; font-weight: 200;
    font-size: 54px; text-transform: uppercase; }
  .featured-title { top: 1505px; color: var(--blue); }
  .listing-card { top: 1592px; width: 500px; height: 207px; background: var(--white); border: 4px solid var(--card-border); }
  .listing-photo { position: absolute; left: 0; top: 0; width: 248px; height: 199px; }
  .listing-caption { position: absolute; left: 0; bottom: 0; width: 248px; height: 40px; background: rgba(20,45,60,0.8);
    color: var(--white); font-family: "Oswald", sans-serif; font-size: 18px; line-height: 40px; text-align: center; }
  .spec-table { position: absolute; left: 258px; top: 4px; width: 226px; font-family: "Oswald", sans-serif; font-size: 17px; border-collapse: collapse; }
  .spec-table td { height: 36.5px; }
  .spec-table th { text-align: left; font-weight: 400; color: var(--blue); }
  .spec-table td { text-align: right; color: #333; }
  .view-all { left: 970px; top: 1822px; width: 144px; height: 41px; border: 2px solid var(--blue); color: var(--blue);
    font-family: "Oswald", sans-serif; font-size: 18px; line-height: 37px; text-align: center; }

  /* Team */
  .team-photo { left: 0; top: 1926px; width: 1200px; height: 417px;
    background: linear-gradient(180deg, #8ab6dc 0%, #b9d2e2 25%, #9fc7c2 45%, #86b5b8 65%, #e6dcc4 85%, #efe7d4 100%); }
  .team-title { top: 1960px; color: #1b1b1b; }
  .team-card { top: 2040px; width: 500px; height: 204px; background: var(--blue); border: 4px solid var(--white); }
  .portrait { position: absolute; left: 0; top: 0; width: 246px; height: 196px; }
  .member { position: absolute; left: 246px; top: 8px; width: 246px; text-align: center; color: var(--white); }
  .member-name { font-family: "Oswald", sans-serif; font-size: 23px; line-height: 30px; }
  .member-role { font-family: "Oswald", sans-serif; font-size: 16px; line-height: 20px; }
  .member-bio { margin: 10px auto 0; width: 214px; font-size: 13px; line-height: 23px; letter-spacing: 1.2px; }
  .read-more { margin: 8px auto 0; width: 148px; height: 42px; border: 2px solid var(--white);
    font-family: "Oswald", sans-serif; font-size: 18px; line-height: 38px; }

  /* Blog */
  .blog-title { top: 2376px; color: var(--blue); }
  .blog-lead { left: 0; top: 2458px; width: 1200px; text-align: center; color: var(--blue-deep);
    font-family: "Oswald", sans-serif; font-size: 17px; }
  .blog-body { left: 150px; top: 2506px; width: 900px; text-align: center; font-size: 14px; line-height: 22px; color: var(--muted); }
  .blog-dots { left: 544px; top: 2585px; width: 112px; height: 20px; }

  /* Footer */
  .site-footer { left: 0; top: 2633px; width: 1200px; height: 107px; background: var(--footer); }
  .social-row { left: 456px; top: 2641px; width: 288px; height: 60px; }
  .copyright { left: 0; top: 2705px; width: 1200px; text-align: center; color: #cfcfcf; font-size: 13px; }
  .copyright strong { color: var(--blue); }
</style>
</head>
<body>

<header>
  <div class="abs hero-photo" role="img" aria-label="Ocean waves breaking on a sandy beach under a blue sky"></div>
  <div class="abs brand-box"><span class="brand-name">Marlow on<br>the Shore</span></div>
  <nav class="abs main-nav">
    <span class="current">Welcome</span><span>Featured Listing</span><span>Previously Sold</span><span>Sell</span>
    <span>Search</span><span>Team</span><span>Videos</span><span>Blog</span><span>Explore O.C</span><span>Contact</span>
  </nav>
  <h1 class="abs hero-title">MARLOW ON THE SHORE</h1>
</header>

<section>
  <div class="abs video-frame" role="img" aria-label="Video still of a resort garden with palms, pavilions and a fountain above the ocean"></div>
  <svg class="abs play-btn" viewBox="0 0 98 62"><rect width="98" height="62" rx="4" fill="rgba(30,30,30,0.75)"/><path d="M42 18 L60 31 L42 44 Z" fill="#fff"/></svg>
  <div class="abs highlights">
    <div class="highlight" style="top:50px"><svg viewBox="0 0 54 54"><circle cx="27" cy="27" r="25" fill="none" stroke="#1a9be6" stroke-width="2"/><path d="M16 27 L24 35 L39 19" fill="none" stroke="#1a9be6" stroke-width="4"/></svg>Quiet and Peaceful Location</div>
    <div class="highlight" style="top:143px"><svg viewBox="0 0 54 54"><circle cx="27" cy="27" r="25" fill="none" stroke="#1a9be6" stroke-width="2"/><path d="M16 27 L24 35 L39 19" fill="none" stroke="#1a9be6" stroke-width="4"/></svg>High Standard Properties</div>
    <div class="highlight" style="top:236px"><svg viewBox="0 0 54 54"><circle cx="27" cy="27" r="25" fill="none" stroke="#1a9be6" stroke-width="2"/><path d="M16 27 L24 35 L39 19" fill="none" stroke="#1a9be6" stroke-width="4"/></svg>Modern Architecture</div>
  </div>
</section>

<section>
  <div class="abs leader-photo" role="img" aria-label="Panoramic view of a coastal resort with lawns, palms and a pergola walkway"></div>
  <div class="abs label-box leader-title">List with the Leader</div>
  <div class="abs label-box sell-btn">Sell Your Home</div>
  <div class="abs label-box buy-btn">Buy Your Home</div>
</section>

<section>
  <div class="abs featured-band"></div>
  <h2 class="abs section-title featured-title">Featured Listing</h2>

  <article class="abs listing-card" style="left:77px">
    <div class="listing-photo" role="img" aria-label="White modern villa with a pool under a blue sky" style="background:linear-gradient(180deg,#3f8fd6 0%,#9fcbe9 45%,#e8ecef 70%,#6a8fa0 100%)"></div>
    <div class="listing-caption">214 Cove Villa</div>
    <table class="spec-table">
      <tr><th>Floor :</th><td>3</td></tr><tr><th>Room:</th><td>10</td></tr><tr><th>Bathrooms:</th><td>7</td></tr>
      <tr><th>Area:</th><td>400m</td></tr><tr><th>Price:</th><td>$ 126, 600.00</td></tr>
    </table>
  </article>

  <article class="abs listing-card" style="left:619px">
    <div class="listing-photo" role="img" aria-label="Modern house at dusk with a lit swimming pool" style="background:linear-gradient(180deg,#1f4f8c 0%,#3c6fa8 40%,#b9b3a3 65%,#2aa7c9 100%)"></div>
    <div class="listing-caption">214 Cove Villa</div>
    <table class="spec-table">
      <tr><th>Floor :</th><td>3</td></tr><tr><th>Room:</th><td>10</td></tr><tr><th>Bathrooms:</th><td>7</td></tr>
      <tr><th>Area:</th><td>400m</td></tr><tr><th>Price:</th><td>$ 126, 600.00</td></tr>
    </table>
  </article>

  <div class="abs view-all">View All</div>
</section>

<section>
  <div class="abs team-photo" role="img" aria-label="Calm beach and turquoise sea with green hills"></div>
  <h2 class="abs section-title team-title">Meet the Team</h2>

  <article class="abs team-card" style="left:77px">
    <div class="portrait" role="img" aria-label="Portrait of the managing director" style="background:linear-gradient(180deg,#8d9aa3,#c9b19a)"></div>
    <div class="member">
      <div class="member-name">Clara Wendell</div>
      <div class="member-role">Managing Director</div>
      <p class="member-bio">Lorem Ipsum is simply dummy text of the printing and typesetting industry.</p>
      <div class="read-more">Read More</div>
    </div>
  </article>

  <article class="abs team-card" style="left:608px">
    <div class="portrait" role="img" aria-label="Portrait of the team leader" style="background:linear-gradient(180deg,#5a4a3c,#8a7a68)"></div>
    <div class="member">
      <div class="member-name">Grant Ellison</div>
      <div class="member-role">Team Leader</div>
      <p class="member-bio">Lorem Ipsum is simply dummy text of the printing and typesetting industry.</p>
      <div class="read-more">Read More</div>
    </div>
  </article>
</section>

<section>
  <h2 class="abs section-title blog-title">Blog</h2>
  <p class="abs blog-lead">Lorem Ipsum is simply dummy text of the printing and typesetting industry.</p>
  <div class="abs blog-body">
    <p>Lorem Ipsum is simply dummy text of the printing and typesetting industry. Lorem Ipsum has been the industry's standard dummy text ever since the 1500sLorem Ipsum is simply dummy text of the printing and typesetting industry.</p>
    <p>25 Feb by Admin</p>
  </div>
  <svg class="abs blog-dots" viewBox="0 0 112 20">
    <circle cx="10" cy="10" r="7.5" fill="#1a9be6"/>
    <circle cx="40" cy="10" r="7" fill="none" stroke="#1a9be6" stroke-width="1.5"/>
    <circle cx="71" cy="10" r="7" fill="none" stroke="#1a9be6" stroke-width="1.5"/>
    <circle cx="101" cy="10" r="7" fill="none" stroke="#1a9be6" stroke-width="1.5"/>
  </svg>
</section>

<footer>
  <div class="abs site-footer"></div>
  <svg class="abs social-row" viewBox="0 0 288 60" aria-label="Social links">
    <circle cx="30" cy="30" r="26" fill="none" stroke="#fff" stroke-width="2.5"/>
    <circle cx="106" cy="30" r="26" fill="none" stroke="#fff" stroke-width="2.5"/>
    <circle cx="181" cy="30" r="26" fill="none" stroke="#fff" stroke-width="2.5"/>
    <circle cx="258" cy="30" r="26" fill="none" stroke="#fff" stroke-width="2.5"/>
  </svg>
  <p class="abs copyright">©2015 <strong>Marlow on the Shore</strong>. All Rights Reserved.</p>
</footer>

</body>
</html>
```